Webbanner-Design für Kaffee-Abo
Zielgruppe
Kaffeeröster mit eigenem Onlineshop
Zielgruppe: Kaffeeliebhaber, die Handgerösteten Kaffee zu einem super Preis finden wollen.
Wir möchten ein Kaffee-Abo für unsere Kunden anbieten, damit Ihnen der Einkauf ihres Lieblingskaffees erleichtert wird. Den Kunden soll es nie wieder passieren, dass die Kaffeebohnen leer sind, also können sie einen eigenen Rhytmus wählen, in dem sie den Kaffee automatisch zugesandt bekommen. Es gibt keine Mindestlaufzeit und das Abo kann jederzeit gekündigt oder unterbrochen werden.
Uns ist ein persönlicher und lockerer Umgang mit unseren Kunden wichtig. Daher soll der Internetauftritt auch locker, freundlich und sympathisch wirken.
Schauen Sie bitte auf unsere Webseite:
www.bohnenwerkstatt-lind.de
Aufgabenstellung
Uns ist wichtig, dass der Banner freundlich und Sympatisch wirkt und Vertrauen vermittelt anstatt Angst vor einem verbindlichen Abo entstehen zu lassen (Unser Abo ist jederzeit unkompliziert kündbar). Der Banner sollte zu unserer Webseite passen.
Unsere Webseite ist unter www.bohnenwerkstatt-lind.de zu finden. Es wird ein neuer „Reiter“ mit dem Titel „Kaffee-Abo“ auf die Webseite implementiert werden. Hierfür möchten wir den Banner von Ihnen gestaltet haben. Der Banner sollte dem Format von unseren anderen Bannern entsprechen. Es besteht auch die Möglichkeit, dass ein 2 bis 3 Teiliger Wechselbanner (Wie auf unserer Startseite) eingebaut wird.

```html
<!DOCTYPE html>
<html lang="de">
<head>
<meta charset="utf-8">
<title>Kaffee-Abo Banner – Bohnenwerkstatt</title>
<link href="https://fonts.googleapis.com/css2?family=Oswald:wght@500;600&family=Permanent+Marker&display=swap" rel="stylesheet">
<style>
  :root{
    --board:#2b2c2e;
    --wood-dark:#2e211b;
    --wood-mid:#4a3428;
    --wood-light:#5a4334;
    --bag:#141414;
    --bag-edge:#262626;
    --label:#ffffff;
    --ink:#111111;
    --text:#ffffff;
    --bean:#5b3a24;
    --bean-dark:#3a2416;
    --seal:#fbf6f2;
    --seal-ring:#b7784f;
  }
  *{box-sizing:border-box;margin:0;padding:0}
  html,body{width:1200px;height:1200px;overflow:hidden;background:var(--board)}
  .board{position:relative;width:1200px;height:1200px}
  .banner{position:absolute;left:65px;width:1069px;height:503px;overflow:hidden}
  .banner--empty-cup{top:76px}
  .banner--hot-tip{top:611px}

  .wood{position:absolute;top:0;bottom:0;
    background:
      repeating-linear-gradient(180deg,rgba(0,0,0,.18) 0 2px,transparent 2px 62px),
      linear-gradient(100deg,var(--wood-dark),var(--wood-mid) 45%,var(--wood-light) 70%,var(--wood-dark));}
  .photo{position:absolute;top:0;bottom:0}
  .banner--empty-cup .wood{left:0;width:576px}
  .banner--empty-cup .photo{left:576px;right:0;
    background:radial-gradient(ellipse at 60% 75%,#3f4d52 0,#28343a 35%,transparent 60%),
      linear-gradient(160deg,#e6e3dc 0,#9a9993 30%,#2a3338 55%,#1c2428 100%)}
  .banner--hot-tip .photo{left:0;width:603px;
    background:radial-gradient(ellipse at 45% 80%,#f1ece6 0,#c8a98e 25%,transparent 50%),
      linear-gradient(150deg,#d9d2cc 0,#b8957a 40%,#8a6a52 75%,#6b4f3d 100%)}
  .banner--hot-tip .wood{left:603px;right:0}

  .brush{position:absolute;font-family:"Permanent Marker",cursive;color:var(--text);
    text-transform:uppercase;text-align:center;line-height:1.05;transform:translateX(-50%);white-space:nowrap}
  .title-abo{left:271px;top:65px;font-size:31px}
  .title-empty{left:821px;top:83px;font-size:60px;line-height:1.1}
  .title-tip{left:240px;top:59px;font-size:60px;line-height:1.15}
  .title-best{left:852px;top:72px;font-size:29px}

  .benefits{position:absolute;list-style:none}
  .benefit{position:absolute;left:0;display:flex;align-items:center;gap:20px;
    font-family:"Oswald",sans-serif;font-weight:500;font-size:17px;line-height:1.3;
    color:var(--text);text-transform:uppercase;white-space:nowrap}
  .benefit svg{flex:none;width:50px;height:44px}
  .benefits--abo{left:140px;top:180px}
  .benefits--quality{left:720px;top:176px}

  .bag{position:absolute;width:234px;height:396px;background:linear-gradient(90deg,var(--bag-edge),var(--bag) 30%,#0b0b0b 70%,var(--bag-edge));
    clip-path:polygon(3% 2%,97% 0,100% 100%,0 100%)}
  .banner--empty-cup .bag{left:457px;top:107px}
  .banner--hot-tip .bag{left:460px;top:109px}
  .bag-brand{position:absolute;top:48px;left:0;right:0;text-align:center;
    font-family:"Oswald",sans-serif;font-weight:500;font-size:13px;letter-spacing:1px;color:var(--text)}
  .bag-valve{position:absolute;top:93px;left:50%;width:22px;height:22px;margin-left:-11px;border-radius:50%;background:#1f1f1f}
  .bag-label{position:absolute;left:67px;top:150px;width:143px;height:200px;background:var(--label);
    padding:12px 10px;font-family:"Oswald",sans-serif;font-weight:600;font-size:34px;line-height:1.02;
    color:var(--ink);text-transform:uppercase;text-align:center}
  .bag-label .inverse{display:block;background:var(--ink);color:var(--label);margin:3px 0 0;padding:2px 0 4px}

  .seal{position:absolute;left:782px;top:355px;width:140px;height:140px}
</style>
</head>
<body>
<main class="board">

  <section class="banner banner--empty-cup">
    <div class="wood" role="img" aria-label="Dunkle Holzbretter als Hintergrund"></div>
    <div class="photo" role="img" aria-label="Foto: leere Kaffeetasse auf Untertasse auf einem Holztisch"></div>
    <h2 class="brush title-abo">Unser<br>Kaffee-Abo:</h2>
    <ul class="benefits benefits--abo">
      <li class="benefit" style="top:0">
        <svg viewBox="0 0 50 44" aria-hidden="true"><ellipse cx="22" cy="24" rx="17" ry="13" fill="var(--bean)" transform="rotate(-20 22 24)"/><path d="M12 22l8 9 20-24" fill="none" stroke="#fff" stroke-width="4.5" stroke-linecap="round" stroke-linejoin="round"/></svg>
        <span>Kaffee, wann immer<br>du ihn brauchst!</span></li>
      <li class="benefit" style="top:92px">
        <svg viewBox="0 0 50 44" aria-hidden="true"><ellipse cx="22" cy="24" rx="17" ry="13" fill="var(--bean)" transform="rotate(-20 22 24)"/><path d="M12 22l8 9 20-24" fill="none" stroke="#fff" stroke-width="4.5" stroke-linecap="round" stroke-linejoin="round"/></svg>
        <span>Flexibel monatlich<br>kündbar!</span></li>
      <li class="benefit" style="top:177px">
        <svg viewBox="0 0 50 44" aria-hidden="true"><ellipse cx="22" cy="24" rx="17" ry="13" fill="var(--bean)" transform="rotate(-20 22 24)"/><path d="M12 22l8 9 20-24" fill="none" stroke="#fff" stroke-width="4.5" stroke-linecap="round" stroke-linejoin="round"/></svg>
        <span>Ohne Mindestlaufzeit!</span></li>
    </ul>
    <div class="bag" role="img" aria-label="Schwarze Kaffeetüte">
      <div class="bag-brand">BOHNENWERKSTATT</div>
      <div class="bag-valve"></div>
      <div class="bag-label">Teste<br>unser<span class="inverse">Kaffee<br>Abo!</span></div>
    </div>
    <h2 class="brush title-empty">Tasse<br>leer?</h2>
  </section>

  <section class="banner banner--hot-tip">
    <div class="photo" role="img" aria-label="Foto: Hand hält dampfende weiße Kaffeetasse vor warmem, unscharfem Hintergrund"></div>
    <div class="wood" role="img" aria-label="Dunkle Holzbretter als Hintergrund"></div>
    <h2 class="brush title-tip">Unser<br>heißester<br>Tipp!</h2>
    <div class="bag" role="img" aria-label="Schwarze Kaffeetüte">
      <div class="bag-brand">BOHNENWERKSTATT</div>
      <div class="bag-valve"></div>
      <div class="bag-label">Teste<br>unser<span class="inverse">Kaffee<br>Abo!</span></div>
    </div>
    <h2 class="brush title-best">Bester Kaffee im<br>unkomplizierten Abo</h2>
    <ul class="benefits benefits--quality">
      <li class="benefit" style="top:0">
        <svg viewBox="0 0 50 44" aria-hidden="true"><ellipse cx="22" cy="24" rx="17" ry="13" fill="var(--bean)" transform="rotate(-20 22 24)"/><path d="M12 22l8 9 20-24" fill="none" stroke="#fff" stroke-width="4.5" stroke-linecap="round" stroke-linejoin="round"/></svg>
        <span>100% fair<br>gehandelter Kaffee</span></li>
      <li class="benefit" style="top:82px">
        <svg viewBox="0 0 50 44" aria-hidden="true"><ellipse cx="22" cy="24" rx="17" ry="13" fill="var(--bean)" transform="rotate(-20 22 24)"/><path d="M12 22l8 9 20-24" fill="none" stroke="#fff" stroke-width="4.5" stroke-linecap="round" stroke-linejoin="round"/></svg>
        <span>Produziert nach höchsten<br>Qualitätsstandarts</span></li>
    </ul>
    <svg class="seal" viewBox="0 0 140 140" role="img" aria-label="Qualitätssiegel">
      <circle cx="70" cy="70" r="68" fill="var(--seal)"/>
      <circle cx="70" cy="70" r="46" fill="none" stroke="var(--seal-ring)" stroke-width="2"/>
    </svg>
  </section>

</main>
</body>
</html>
```